WordPress Classical Pianist Website, one pager with one one-pager as a subsite

Hi everyone,

I'm looking for a long-term freelance designer to refresh and modernize my existing WordPress website (www.talvenor.com).
The new layout should be a clean one-page design with one one-pager subpage (CD's subpage).

From time to time, I also need help with smaller design projects such as concert flyers, CD covers (including booklets), and other promotional materials — that’s why I’m looking for a long-term collaboration.

The website is fully functional; I just need a fresh visual update that matches the style of my new CD and future materials.

Experience with WordPress is essential.
I'm looking for someone reliable, creative, and easy to communicate with — not a large agency.

Thanks a lot!
Roland

Target Market(s)

Classical music audience, concert organizers (!), music students/music universities and piano music lovers worldwide.

Industry/Entity Type

Classical Music / Artist Portfolio

Coding

Coded - Design and coding required

Number of Pages Required

2 page

Font styles to use
Other font styles liked:
• Ephesis Bold, Lexend Tera, Lexend Tera Medium, Adobe Fnt23

Requirements
Must have
• Clean and elegant one-page layout with 1–2 subpages (Bio, Concerts, Contact); high-quality visual design reflecting a professional concert pianist’s identity; visual harmony with my new CD “Ombre sul Lago Fermo” (colors, mood, tone); integration of photos, videos, CD covers, and short audio samples via a mini audio player; all existing content to be transferred from www.talvenor.com ; bilingual structure (German/English); responsive design (desktop + mobile); built on WordPress
Nice to have
• Subtle animations or transitions between sections (smooth scrolling or fade-ins), elegant typography inspired by classical music aesthetics (fonts below), optional dark / light mode design, small music/video player or integrated streaming links (Sonora, Cadenza, Vidora)
Should not have
• Overloaded or cluttered layout, flashy or bright color schemes, stock photos unrelated to piano or classical music, heavy animations or slow loading times, generic, template-looking WordPress themes

```html
<!DOCTYPE html>
<html lang="en">
<head>
<meta charset="utf-8">
<title>Roland Talvenor — Concert Pianist</title>
<link rel="stylesheet" href="https://fonts.googleapis.com/css2?family=Lexend+Exa:wght@500;700&family=Roboto+Condensed:wght@500;600;700&family=Heebo:wght@400;500;600&display=swap">
<style>
:root{
  --ink:#1b2130;
  --ink-deep:#141925;
  --band-dark:#15171c;
  --gold:#b8893a;
  --gold-soft:#c9a05a;
  --gold-band:#c29648;
  --orange:#f26a1b;
  --cream:#f4e7d0;
  --paper:#ffffff;
  --text:#4a4a4a;
  --rule:#e4d6bd;
}
*{box-sizing:border-box;margin:0;padding:0}
html,body{width:1200px;height:4468px;overflow:hidden}
body{position:relative;background:var(--paper);font-family:"Heebo",sans-serif;color:var(--text)}
a{text-decoration:none}
.abs{position:absolute}
.display{font-family:"Lexend Exa",sans-serif;font-weight:700;text-transform:uppercase;white-space:nowrap;letter-spacing:0;line-height:1}
.kicker{font-family:"Roboto Condensed",sans-serif;font-weight:600;text-transform:uppercase;color:var(--gold);white-space:nowrap;line-height:1}
.center{left:0;width:1200px;text-align:center}

/* flat bands standing in for the keyboard motif */
.band{position:absolute;left:0;width:1200px}
.band-dark{background:var(--band-dark)}
.band-gold{background:var(--gold-band)}

/* hero */
.hero{position:absolute;left:0;top:0;width:1200px;height:543px;background:radial-gradient(ellipse at 30% 40%,#2a3142 0%,var(--ink) 55%,var(--ink-deep) 100%)}
.brand{left:112px;top:34px;font-family:"Lexend Exa",sans-serif;font-weight:700;font-size:24px;color:#fff;letter-spacing:1px;line-height:1}
.nav a{position:absolute;top:42px;font-family:"Roboto Condensed",sans-serif;font-weight:600;font-size:16px;line-height:1;color:#fff;white-space:nowrap}
.nav a.active{color:var(--gold-soft)}
.social-sq{width:32px;height:32px;background:var(--gold)}
.lang{left:1104px;top:43px;font-family:"Roboto Condensed",sans-serif;font-weight:600;font-size:14px;line-height:1;color:#fff;white-space:nowrap}
.lang .on{color:var(--gold-soft)}
.hero-photo{left:199px;top:113px;width:346px;height:430px;background:linear-gradient(160deg,#3a2d2a 0%,#8a5a45 40%,#222 75%,#14171f 100%)}
.hero-rule{left:544px;top:135px;width:2px;height:408px;background:var(--gold)}
.hero-title{left:588px;top:154px;font-size:44px;color:#fff}
.hero-title2{left:588px;top:208px;font-size:52px;color:var(--gold-soft)}
.hero-sub{left:591px;top:277px;font-family:"Lexend Exa",sans-serif;font-weight:700;font-size:15px;line-height:1;color:#fff;white-space:nowrap}
.hero-bar{left:543px;top:316px;width:463px;height:54px;background:var(--orange);color:#fff;font-family:"Roboto Condensed",sans-serif;font-weight:600;font-size:19px;line-height:54px;padding-left:46px;white-space:nowrap}
.hero-text{left:590px;top:383px;width:420px;font-size:15.5px;line-height:28px;color:#e8e8e8}
.btn{display:flex;align-items:center;justify-content:center;gap:10px;font-family:"Heebo",sans-serif;font-weight:500;font-size:15px;white-space:nowrap}
.btn-gold{background:var(--gold);color:#fff}
.btn-line{border:1.5px solid var(--gold);color:var(--gold-soft)}

/* album */
.album-kicker{top:708px;font-size:27px}
.album-title{top:746px;font-size:40px;color:var(--ink)}
.disc{left:630px;top:868px;width:265px;height:265px;border-radius:50%;background:radial-gradient(circle,#fff 0 10%,#cfcfcf 11% 14%,#e6e6e6 15%,#d2d2d2 60%,#bdbdbd 100%)}
.cover{left:303px;top:838px;width:410px;height:411px;background:linear-gradient(135deg,#e7c88f 0%,#c9a06a 45%,#6a4a35 70%,#1c1c1c 100%);box-shadow:0 8px 24px rgba(0,0,0,.22)}
.album-text{top:1294px;font-size:17px;line-height:30px;color:#555}
.tracks-label{top:1388px;font-family:"Roboto Condensed",sans-serif;font-weight:700;font-size:17px;line-height:1;color:#222}
.track{top:1425px;height:49px;background:var(--cream);border:1px solid var(--rule);color:var(--gold);font-size:14.5px}
.track .dot{width:14px;height:14px;border-radius:50%;background:var(--gold)}
.stream-label{top:1510px;font-size:17px}
.stream{top:1543px;height:87px;background:#fff;border:1px solid #eee;box-shadow:0 3px 10px rgba(0,0,0,.12);font-family:"Heebo",sans-serif;font-weight:600;font-size:30px;color:var(--ink)}

/* videos */
.video-band{position:absolute;left:0;top:1803px;width:1200px;height:668px;background:linear-gradient(180deg,#b88a3c 0%,#b3843a 60%,#a87a33 100%)}
.video-kicker{top:1868px;font-size:26px;color:#fff}
.video-title{top:1908px;font-size:41px;color:#fff}
.video-word{left:178px;top:2362px;font-family:"Lexend Exa",sans-serif;font-weight:700;font-size:74px;line-height:1;color:rgba(255,255,255,.12);text-transform:uppercase;transform:rotate(-90deg);transform-origin:0 0;white-space:nowrap}
.video-frame{left:272px;top:1997px;width:654px;height:366px;background:linear-gradient(90deg,#f4e3c2 0%,#e3bf86 45%,#b98a55 75%,#8f6642 100%)}
.play{left:578px;top:2158px;width:44px;height:44px;border-radius:50%;background:var(--ink-deep)}
.dots{display:flex;gap:6px}
.dots span{width:8px;height:8px;border-radius:50%;background:#ddd}
.dots span.on{background:#fff;box-shadow:0 0 0 1px #999}

/* about */
.about-photo{left:113px;top:2672px;width:485px;height:564px;background:linear-gradient(150deg,#f2f2f2 0%,#8a8a8a 40%,#2a2a2a 70%,#0e0e0e 100%)}
.about-kicker{left:677px;top:2706px;font-size:27px}
.about-title{left:675px;top:2746px;font-size:42px;color:var(--ink)}
.about-text{left:677px;top:2810px;width:412px;font-size:14.5px;line-height:29px;color:#555;text-align:justify}
.about-btn{left:677px;top:3156px;width:133px;height:43px;font-size:14.5px}

/* concerts */
.concert-kicker{top:3346px;font-size:27px}
.concert-title{top:3386px;font-size:42px;color:var(--ink)}
.card{top:3465px;height:419px;background:#fff;border:1px solid #eee4d2;box-shadow:0 3px 12px rgba(0,0,0,.08)}
.card.featured{border:2px solid var(--gold)}
.card-img{position:absolute;left:4px;top:4px;right:4px;height:218px}
.card-rule{position:absolute;left:24px;top:222px;width:3px;height:180px;background:var(--gold)}
.card-date{position:absolute;left:56px;top:250px;font-size:14px;line-height:22px;color:var(--gold);font-weight:500}
.card-work{position:absolute;left:56px;top:300px;font-size:14px;line-height:23px;color:#333}
.card-work b{font-weight:600;color:#111}
.card-btn{position:absolute;left:56px;top:361px;width:124px;height:34px;font-size:13px}
.btn-dark{background:var(--ink);color:#fff}

/* footer */
.footer{position:absolute;left:0;top:4096px;width:1200px;height:372px;background:radial-gradient(ellipse at 50% 20%,#262d3d 0%,var(--ink) 55%,var(--ink-deep) 100%)}
.foot-brand{top:4196px;font-family:"Lexend Exa",sans-serif;font-weight:700;font-size:28px;line-height:1;color:#fff;letter-spacing:1px}
.foot-nav{position:absolute;top:4288px;left:0;width:1200px;display:flex;justify-content:center;align-items:center;font-family:"Roboto Condensed",sans-serif;font-weight:600;font-size:18px;line-height:1;color:#fff}
.foot-nav span{padding:0 40px}
.foot-nav .sep{width:2px;height:18px;background:#fff}
.foot-nav .active{color:var(--gold-soft)}
.foot-line{left:222px;top:4397px;width:756px;height:1px;background:#6b6f7a}
.gotop{left:867px;top:4380px;width:109px;height:38px;font-size:13.5px}
.copyright{top:4426px;font-size:14px;line-height:1;color:#fff}
</style>
</head>
<body>

<!-- Hero -->
<header class="hero">
  <div class="abs brand">TALVENOR</div>
  <nav class="nav">
    <a class="active" style="left:513px">HOME</a>
    <a style="left:598px">BIOGRAPHY</a>
    <a style="left:725px">PRESS</a>
    <a style="left:813px">MEDIA</a>
    <a style="left:902px">CONTACT</a>
  </nav>
  <div class="abs social-sq" style="left:1008px;top:35px" role="img" aria-label="Social profile link"></div>
  <div class="abs social-sq" style="left:1054px;top:35px" role="img" aria-label="Professional network link"></div>
  <div class="abs lang"><span class="on">EN</span> | DE</div>

  <div class="abs hero-photo" role="img" aria-label="Portrait of Roland Talvenor in a dark suit"></div>
  <div class="abs hero-rule"></div>
  <div class="abs display hero-title">Immediate</div>
  <div class="abs display hero-title2">Impression</div>
  <div class="abs hero-sub">OF ARTISTRY &amp; PROFESSIONALISM</div>
  <div class="abs hero-bar">ROLAND TALVENOR — CONCERT PIANIST</div>
  <p class="abs hero-text">Roland Talvenor is an artist of profound musical insight and technical brilliance.</p>
  <a class="abs btn btn-gold" style="left:590px;top:454px;width:119px;height:42px">
    <svg width="16" height="14" viewBox="0 0 16 14"><path d="M2 9V7a6 6 0 0 1 12 0v2" fill="none" stroke="#fff" stroke-width="1.8"/><rect x="1" y="8" width="3.5" height="5" rx="1" fill="#fff"/><rect x="11.5" y="8" width="3.5" height="5" rx="1" fill="#fff"/></svg>
    Listen</a>
  <a class="abs btn btn-line" style="left:735px;top:454px;width:146px;height:42px">
    <svg width="14" height="14" viewBox="0 0 14 14" fill="var(--gold-soft)"><circle cx="7" cy="3" r="2"/><circle cx="3" cy="10" r="2"/><circle cx="11" cy="10" r="2"/></svg>
    Concerts</a>
</header>
<div class="band band-dark" style="top:543px;height:85px" role="img" aria-label="Decorative keyboard band"></div>

<!-- Latest album -->
<section>
  <div class="abs center kicker album-kicker">Roland Talvenor’s Latest Album</div>
  <h2 class="abs center display album-title">Ombre sul Lago Fermo</h2>
  <div class="abs disc" role="img" aria-label="Compact disc sliding out of the sleeve"></div>
  <div class="abs cover" role="img" aria-label="Album cover of Ombre sul Lago Fermo with the pianist leaning on a piano"></div>
  <p class="abs center album-text">Inspired by Halverson’s visionary sonata, this recording explores the fine line between<br>structure and imagination — between dream and form.</p>
  <div class="abs center tracks-label">LISTEN TO SELECTED TRACKS:</div>
  <a class="abs btn track" style="left:244px;width:205px"><span class="dot"></span>Prelude &amp; Fantasy</a>
  <a class="abs btn track" style="left:475px;width:228px"><span class="dot"></span>Nocturne in C# minor</a>
  <a class="abs btn track" style="left:732px;width:223px"><span class="dot"></span>Adagio con Fantasia</a>
  <div class="abs center kicker stream-label">Stream on:</div>
  <a class="abs btn stream" style="left:302px;width:180px">Sonora</a>
  <a class="abs btn stream" style="left:503px;width:182px">Cadenza</a>
  <a class="abs btn stream" style="left:717px;width:181px">Vidora</a>
</section>

<!-- Videos -->
<section>
  <div class="band band-gold" style="top:1713px;height:90px" role="img" aria-label="Decorative keyboard band"></div>
  <div class="video-band" role="img" aria-label="Warm gold backdrop of a grand piano interior"></div>
  <div class="abs center kicker video-kicker">Morel: Jeux d’eau</div>
  <h2 class="abs center display video-title">Live from Halden Konzerthaus</h2>
  <div class="abs video-word">Videos</div>
  <div class="abs video-frame" role="img" aria-label="Video still: album artwork with the pianist in profile"></div>
  <div class="abs play"><svg width="44" height="44" viewBox="0 0 44 44"><path d="M18 15l11 7-11 7z" fill="#fff"/></svg></div>
  <div class="abs dots" style="left:568px;top:2401px"><span class="on"></span><span></span><span></span><span></span><span></span></div>
  <div class="band band-gold" style="top:2471px;height:57px" role="img" aria-label="Decorative keyboard band"></div>
</section>

<!-- About -->
<section>
  <div class="abs about-photo" role="img" aria-label="Black and white portrait of the pianist seated at a grand piano"></div>
  <div class="abs kicker about-kicker">About Roland</div>
  <h2 class="abs display about-title">Explore More</h2>
  <div class="abs about-text">
    <p>Roland Talvenor, a pianist of international renown, first gained worldwide attention when he won the first prize at the prestigious Northgate Piano Competition in London in 1994. This victory, coupled with the award for the best Valen interpretation, opened doors to significant concert stages in the United Kingdom, Germany, Italy, Japan, and the United States.</p>
    <p style="margin-top:29px">As a soloist, he performed with renowned orchestras such as the Thamesbury Symphony Orchestra, The Aurelian Orchestra, the Western Isles Chamber Orchestra.</p>
  </div>
  <a class="abs btn btn-gold about-btn">Explore More</a>
</section>

<!-- Concerts -->
<section>
  <div class="abs center kicker concert-kicker">Experience Ombre sul Lago Fermo live.</div>
  <h2 class="abs center display concert-title">Upcoming Concerts</h2>

  <article class="abs card" style="left:113px;width:308px">
    <div class="card-img" role="img" aria-label="Close-up of hands on piano keys" style="background:linear-gradient(135deg,#2a1d17 0%,#6e4a36 45%,#d9c3a5 75%,#3a2a22 100%)"></div>
    <div class="card-rule"></div>
    <div class="card-date">10 NOV 2025<br>VIENNA, KLANGHALLE</div>
    <div class="card-work">Halverson, Lindqvist, Talvenor:<br><b>Ombre sul Lago Fermo</b></div>
    <a class="card-btn btn btn-gold">View Details</a>
  </article>

  <article class="abs card featured" style="left:444px;width:314px">
    <div class="card-img" role="img" aria-label="Grand piano under a spotlight on an empty stage" style="background:radial-gradient(ellipse at 50% 35%,#7f94a6 0%,#2c3a48 45%,#0f151d 100%)"></div>
    <div class="card-rule"></div>
    <div class="card-date">10 NOV 2025<br>VIENNA, KLANGHALLE</div>
    <div class="card-work">Halverson, Lindqvist, Talvenor:<br><b>Ombre sul Lago Fermo</b></div>
    <a class="card-btn btn btn-dark">View Details</a>
  </article>

  <article class="abs card" style="left:777px;width:310px">
    <div class="card-img" role="img" aria-label="Album artwork with the pianist leaning on a piano" style="background:linear-gradient(120deg,#f1ddb8 0%,#d9b47c 50%,#8c6644 80%,#2a211c 100%)"></div>
    <div class="card-rule"></div>
    <div class="card-date">10 NOV 2025<br>VIENNA, KLANGHALLE</div>
    <div class="card-work">Halverson, Lindqvist, Talvenor:<br><b>Ombre sul Lago Fermo</b></div>
    <a class="card-btn btn btn-gold">View Details</a>
  </article>

  <div class="abs dots" style="left:568px;top:3915px"><span class="on" style="background:#222;box-shadow:none"></span><span></span><span></span><span></span><span></span></div>
</section>

<!-- Footer -->
<div class="band band-dark" style="top:4005px;height:91px" role="img" aria-label="Decorative keyboard band"></div>
<footer class="footer"></footer>
<div class="abs center foot-brand">TALVENOR</div>
<nav class="foot-nav">
  <span class="active">HOME</span><i class="sep"></i>
  <span>BIOGRAPHY</span><i class="sep"></i>
  <span>PRESS</span><i class="sep"></i>
  <span>MEDIA</span><i class="sep"></i>
  <span>CONTACT US</span>
</nav>
<div class="abs social-sq" style="left:561px;top:4342px;width:30px;height:30px" role="img" aria-label="Social profile link"></div>
<div class="abs social-sq" style="left:608px;top:4342px;width:30px;height:30px" role="img" aria-label="Professional network link"></div>
<div class="abs foot-line"></div>
<a class="abs btn btn-gold gotop">
  <svg width="12" height="12" viewBox="0 0 12 12"><path d="M6 1L1 7h3v4h4V7h3z" fill="#fff"/></svg>Go Top</a>
<div class="abs center copyright">(C) Copyright 2025 | All Rights Reserved</div>

</body>
</html>
```